IT services company needs a business card designed

-2 sided business card.-Front is going to be the logo raised (3D floating effect) on a black background. Make the logos spider web shiny silver and keep the spider the same design. -Back needs to have the following information:Doug Farrow, Managing Partner, Cell: 602-488-3179, Website: Kolvantra.com, Email: Doug@Kolvantra.com
Target Market(s)
IT Services
Industry/Entity Type
It Company
Contact Information for Business Card
-2 sided business card.
-Front is going to be the logo raised (3D floating effect) on a black background. Make the logos spider web shiny silver and keep the spider the same design.
-Back needs to have the following information:
Doug Farrow, Managing Partner, Cell: 602-488-3179, Website: Kolvantra.com, Email: Doug@Kolvantra.com
Look and feel

```html
<!DOCTYPE html>
<html lang="en">
<head>
<meta charset="utf-8">
<title>Kolvantra – Business Card</title>
<link href="https://fonts.googleapis.com/css2?family=Montserrat:wght@400;500;600&display=swap" rel="stylesheet">
<style>
  :root {
    --canvas-bg: #2b2f35;
    --card-black: #0d0e10;
    --card-black-edge: #1b1d21;
    --card-white: #ffffff;
    --brand-blue: #1a93dd;
    --web-silver: #b8bcc2;
    --text-dark: #2a2c30;
    --text-grey: #6b6e73;
    --logo-white: #f4f5f7;
  }
  * { margin: 0; padding: 0; box-sizing: border-box; }
  html, body {
    width: 1200px; height: 900px; overflow: hidden;
    background: var(--canvas-bg);
    font-family: "Montserrat", sans-serif;
  }
  .stage {
    width: 1200px; height: 900px;
    display: flex; align-items: center; justify-content: center; gap: 40px;
  }
  .card {
    position: relative;
    width: 540px; height: 309px;
    border-radius: 18px;
    overflow: hidden;
    box-shadow: 0 18px 40px rgba(0,0,0,.45);
  }

  /* Back side: contact details */
  .card--back { background: var(--card-white); }
  .web-corner {
    position: absolute; left: 0; top: 0;
    width: 230px; height: 309px;
    background:
      radial-gradient(ellipse at 20% 35%, rgba(26,147,221,.55) 0%, rgba(26,147,221,.25) 35%, rgba(184,188,194,.18) 60%, rgba(255,255,255,0) 78%);
  }
  .contact-block {
    position: absolute; right: 34px; bottom: 30px;
    text-align: right;
  }
  .brand-lockup {
    display: flex; align-items: center; justify-content: flex-end; gap: 8px;
    margin-bottom: 14px;
  }
  .brand-lockup__name {
    font-weight: 500; font-size: 17px; letter-spacing: 2px;
    color: var(--text-dark);
  }
  .brand-lockup__dot {
    width: 9px; height: 9px; border-radius: 50%;
    background: var(--brand-blue);
  }
  .person__name {
    font-weight: 600; font-size: 21px; letter-spacing: .5px;
    color: var(--brand-blue); text-transform: uppercase;
  }
  .person__role {
    font-size: 13px; color: var(--text-grey); margin: 2px 0 12px;
  }
  .contact-list { list-style: none; }
  .contact-list li {
    display: flex; align-items: center; justify-content: flex-end; gap: 10px;
    font-size: 13px; color: var(--text-dark); line-height: 1.6;
  }
  .contact-list svg { width: 13px; height: 13px; fill: var(--brand-blue); }

  /* Front side: logo on black */
  .card--front {
    background: radial-gradient(ellipse at 50% 45%, var(--card-black-edge) 0%, var(--card-black) 70%);
  }
  .web-backdrop {
    position: absolute; inset: 0;
    background: radial-gradient(circle at 50% 45%, rgba(255,255,255,.05) 0%, rgba(255,255,255,0) 60%);
  }
  .front-logo {
    position: absolute; left: 50%; top: 50%;
    transform: translate(-50%, -50%);
    display: flex; align-items: center; gap: 12px;
  }
  .front-logo__name {
    font-weight: 500; font-size: 40px; letter-spacing: 4px;
    color: var(--logo-white);
  }
  .front-logo__dot {
    width: 14px; height: 14px; border-radius: 50%;
    background: var(--brand-blue);
  }
</style>
</head>
<body>
<main class="stage">
  <section class="card card--back">
    <div class="web-corner" role="img" aria-label="Blue and silver spider web with a circuit-style spider in the corner"></div>
    <div class="contact-block">
      <div class="brand-lockup">
        <span class="brand-lockup__dot"></span>
        <span class="brand-lockup__name">KOLVANTRA</span>
      </div>
      <h1 class="person__name">Doug Farrow</h1>
      <p class="person__role">Managing Partner</p>
      <ul class="contact-list">
        <li>602-488-3179
          <svg viewBox="0 0 16 16"><path d="M3.6 1.5l2.3 2.8-1.4 1.7c.9 2 2.5 3.6 4.5 4.5l1.7-1.4 2.8 2.3-1.3 2.2C7 13.4 2.6 9 1.4 2.8z"/></svg>
        </li>
        <li>Kolvantra.com
          <svg viewBox="0 0 16 16"><path d="M1 7.5L15 1l-4 14-3-5.5z"/></svg>
        </li>
        <li>Doug@Kolvantra.com
          <svg viewBox="0 0 16 16"><path d="M8 1a7 7 0 100 14A7 7 0 008 1zm0 1.5c.7 0 1.6 1.4 1.9 3.7H6.1C6.4 3.9 7.3 2.5 8 2.5zM2.6 7.3h2.3v1.4H2.6zm3.5 0h3.8v1.4H6.1zm5 0h2.3v1.4h-2.3zM6.1 9.8h3.8C9.6 12.1 8.7 13.5 8 13.5S6.4 12.1 6.1 9.8z"/></svg>
        </li>
      </ul>
    </div>
  </section>

  <section class="card card--front">
    <div class="web-backdrop" role="img" aria-label="Faint spider web pattern across the black card"></div>
    <div class="front-logo">
      <span class="front-logo__name">KOLVANTRA</span>
      <span class="front-logo__dot"></span>
    </div>
  </section>
</main>
</body>
</html>
```